Design Packaging for Monte Alba Coffee

Please look at website at www.montealbacoffeecompany.example
Need packaging for new coffee company. The size is: 6 x 9 x 3"

```html
<!DOCTYPE html>
<html lang="en">
<head>
<meta charset="utf-8">
<title>Monte Alba Coffee – Costa Rica Organic Coffee Pouch</title>
<link rel="stylesheet" href="https://fonts.googleapis.com/css2?family=Bebas+Neue&family=Poppins:wght@400;700&display=swap">
<style>
  :root {
    --backdrop: #b9b9b9;
    --magenta: #d9125a;
    --jungle: #138f6e;
    --leaf-light: #22b46c;
    --leaf-deep: #1d7463;
    --sun-yellow: #f6b93b;
    --indigo: #37307f;
    --white: #ffffff;
    --roast-brown: #3b2a21;
    --map-tint: #e9e8f3;
  }
  * { margin: 0; padding: 0; box-sizing: border-box; }
  html, body {
    width: 800px; height: 1200px; overflow: hidden;
    background: var(--backdrop);
  }
  .sheet {
    position: relative; width: 800px; height: 1200px;
  }
  .panel {
    position: absolute; top: 331px;
    width: 360px; height: 538px; overflow: hidden;
    background: var(--magenta);
  }
  .panel--front { left: 25px; }
  .panel--back { left: 415px; }
  .panel__art {
    position: absolute; inset: 0; width: 360px; height: 538px;
  }

  /* Front */
  .brand-band {
    position: absolute; left: 0; top: 197px; width: 360px; height: 68px;
    background: var(--white);
    display: flex; align-items: center; justify-content: center; gap: 10px;
  }
  .brand-band__dot {
    width: 22px; height: 22px; border-radius: 50%;
    background: var(--roast-brown);
  }
  .brand-band__name {
    font-family: 'Bebas Neue', sans-serif;
    font-size: 32px; letter-spacing: 1px; line-height: 1;
    color: var(--roast-brown); padding-top: 3px;
  }
  .origin-band {
    position: absolute; left: 0; top: 265px; width: 360px; height: 161px;
    background: var(--indigo); color: var(--white);
  }
  .origin-band__map {
    position: absolute; left: 45px; top: 5px; width: 105px; height: 100px;
  }
  .origin-band__divider {
    position: absolute; left: 187px; top: 0; width: 1px; height: 106px;
    background: var(--white);
  }
  .origin-band__info {
    position: absolute; left: 196px; top: 9px; width: 160px;
  }
  .origin-band__country {
    font-family: 'Bebas Neue', sans-serif;
    font-size: 40px; line-height: 0.95;
  }
  .origin-band__type {
    font-family: 'Poppins', sans-serif; font-weight: 700;
    font-size: 13.5px; letter-spacing: 0.3px; margin-top: 2px;
  }
  .origin-band__notes {
    font-family: 'Poppins', sans-serif; font-weight: 400;
    font-size: 10px; line-height: 11.5px; margin-top: 2px;
  }
  .origin-band__fact {
    position: absolute; left: 29px; top: 106px; width: 303px; height: 32px;
    border-top: 1px solid var(--white); border-bottom: 1px solid var(--white);
    font-family: 'Poppins', sans-serif; font-size: 9.6px; line-height: 11.5px;
    text-align: center; padding-top: 3px;
  }

  /* Back */
  .story {
    position: absolute; left: 90px; top: 190px; width: 170px; color: var(--white);
  }
  .story__heading {
    font-family: 'Bebas Neue', sans-serif;
    font-size: 18.5px; line-height: 21.5px; letter-spacing: 0.2px;
  }
  .story__body {
    font-family: 'Poppins', sans-serif; font-weight: 400;
    font-size: 9.4px; line-height: 10.85px; margin-top: 6px;
  }
</style>
</head>
<body>
<main class="sheet">

  <!-- Front of pouch -->
  <section class="panel panel--front">
    <svg class="panel__art" viewBox="0 0 636 950" preserveAspectRatio="none">
      <defs>
        <linearGradient id="front-canopy" x1="0" y1="0" x2="1" y2="0.4">
          <stop offset="0" stop-color="#f0b544"/>
          <stop offset="0.35" stop-color="#2cae5a"/>
          <stop offset="0.75" stop-color="#1d7463"/>
          <stop offset="1" stop-color="#c81a55"/>
        </linearGradient>
        <linearGradient id="front-ground" x1="0" y1="0" x2="1" y2="1">
          <stop offset="0" stop-color="#22b46c"/>
          <stop offset="0.5" stop-color="#1d8a66"/>
          <stop offset="0.8" stop-color="#c81a55"/>
          <stop offset="1" stop-color="#22b46c"/>
        </linearGradient>
      </defs>
      <path d="M0 195 Q318 60 636 215 L636 950 L0 950 Z" fill="var(--jungle)"/>
      <g role="img" aria-label="Tropical leaves, palm fronds and hibiscus flowers above the brand band">
        <path d="M0 260 C40 210 70 170 90 110 C120 160 150 190 190 180 C230 170 270 140 300 180 C330 150 360 120 400 170 C430 140 470 190 520 200 C560 210 600 230 636 250 L636 350 L0 350 Z" fill="url(#front-canopy)" opacity="0.9"/>
      </g>
      <g role="img" aria-label="Tropical leaves, ferns and hibiscus flowers along the base">
        <rect x="0" y="753" width="636" height="197" fill="url(#front-ground)" opacity="0.85"/>
      </g>
    </svg>

    <div class="brand-band">
      <span class="brand-band__dot"></span>
      <span class="brand-band__name">Monte Alba Coffee</span>
    </div>

    <div class="origin-band">
      <svg class="origin-band__map" viewBox="0 0 105 100" role="img" aria-label="Map silhouette of Costa Rica">
        <rect x="0" y="0" width="105" height="100" rx="6" fill="var(--map-tint)" opacity="0.85"/>
      </svg>
      <span class="origin-band__divider"></span>
      <div class="origin-band__info">
        <h1 class="origin-band__country">Costa Rica</h1>
        <p class="origin-band__type">ORGANIC COFFEE</p>
        <p class="origin-band__notes">Rich in flavor, smooth, and contain an exceptional balance of sweetness</p>
      </div>
      <p class="origin-band__fact">Arabica beans from Costa Rica retain more heart-healthy antioxidants than other varieties</p>
    </div>
  </section>

  <!-- Back of pouch -->
  <section class="panel panel--back">
    <svg class="panel__art" viewBox="0 0 636 950" preserveAspectRatio="none">
      <defs>
        <linearGradient id="back-left" x1="0" y1="0" x2="0" y2="1">
          <stop offset="0" stop-color="#f0b544"/>
          <stop offset="0.3" stop-color="#2cae5a"/>
          <stop offset="1" stop-color="#1d7463"/>
        </linearGradient>
        <linearGradient id="back-right" x1="0" y1="0" x2="0" y2="1">
          <stop offset="0" stop-color="#f0b544"/>
          <stop offset="0.35" stop-color="#1d8a66"/>
          <stop offset="0.75" stop-color="#c81a55"/>
          <stop offset="1" stop-color="#c81a55"/>
        </linearGradient>
        <linearGradient id="back-ground" x1="0" y1="0" x2="1" y2="0">
          <stop offset="0" stop-color="#22b46c"/>
          <stop offset="0.45" stop-color="#c81a55"/>
          <stop offset="0.6" stop-color="#f0b544"/>
          <stop offset="1" stop-color="#22b46c"/>
        </linearGradient>
      </defs>
      <path d="M0 195 Q318 60 636 215 L636 950 L0 950 Z" fill="var(--jungle)"/>
      <g role="img" aria-label="Tropical foliage, palm fronds and hibiscus flowers framing the panel">
        <path d="M0 190 C60 180 140 200 200 210 C150 260 110 300 90 360 C70 480 80 620 60 760 L0 760 Z" fill="url(#back-left)" opacity="0.85"/>
        <path d="M636 250 C580 260 500 250 420 270 C490 330 540 380 560 470 C560 560 520 620 480 680 C540 760 600 830 636 880 Z" fill="url(#back-right)" opacity="0.85"/>
        <path d="M0 780 C80 750 160 770 240 740 C320 770 400 760 480 780 C560 800 600 790 636 800 L636 950 L0 950 Z" fill="url(#back-ground)" opacity="0.85"/>
      </g>
    </svg>

    <div class="story">
      <h2 class="story__heading">MONTE ALBA COFFEE IS ABOUT MORE THAN JUST GREAT TASTING COFFEE...</h2>
      <p class="story__body">It’s about living life to its fullest and supporting others who are doing the same. Monte Alba offers customers the opportunity to taste world class coffee at an affordable price. We work directly with coffee growers in Costa Rica to ensure we bring you a product of unparalleled quality. Not only do we give back to local communities, but also believe strongly in building a company that cares about people from top to bottom.</p>
    </div>
  </section>

</main>
</body>
</html>
```